card design for engineering consultancy

engineering drafting and project management company the provides drafting services for.
Electrical, Hydraulic, Mechanical, and Civil services
The company is called Q7R Services and logo is as attached
Information on card should be.
1. Logo
2.website : Q7RServices.example
3. email : info@Q7RServices.example
4. Phone: (+61) 400512836
5. Motto: Sketch - Detail - Refine - Complete

this card should be basically used for business identification only

Target Market(s)

electricians plumbers air conditioning installers and civil contractors

Industry/Entity Type

engineering, drafting, electrical, plumbing, airconditioning, civil

Contact Information for Business Card

1. Logo 2.website : Q7RServices.example 3. email : info@Q7RServices.example 4. Phone: (+61) 400512836 5. Motto: Sketch - Detail - Refine - Complete

Font styles to use
Serif

Requirements
Must have
• logo
Nice to have
• something inovative and different that makes it stand out from being just another business card

```html
<!DOCTYPE html>
<html lang="en">
<head>
<meta charset="utf-8">
<title>Q7R Services – Business Card</title>
<link href="https://fonts.googleapis.com/css2?family=Roboto:wght@400;500;700;900&family=Roboto+Condensed:wght@700&display=swap" rel="stylesheet">
<style>
  :root {
    --page-bg: #f4f4f4;
    --card-white: #ffffff;
    --brand-red: #d32030;
    --ink-dark: #3f3f41;
    --ink-body: #2b2b2b;
    --card-dark-top: #424242;
    --card-dark-bottom: #232323;
    --rule-grey: #8a8a8a;
  }
  * { box-sizing: border-box; margin: 0; padding: 0; }
  html, body {
    width: 800px; height: 1200px; overflow: hidden;
    background: var(--page-bg);
    font-family: "Roboto", Arial, sans-serif;
  }
  .sheet {
    width: 800px; height: 1200px;
    display: flex; flex-direction: column; align-items: center; justify-content: center;
    gap: 60px;
  }
  .card {
    position: relative;
    width: 560px; height: 320px;
    box-shadow: 6px 10px 14px rgba(0,0,0,0.28);
    overflow: hidden;
  }
  /* Front */
  .card--front { background: var(--card-white); }
  .accent-band {
    position: absolute; left: 18px; top: 68px;
    width: 72px; height: 212px;
    background: var(--brand-red);
  }
  .contact-list {
    position: absolute; left: 112px; top: 162px;
    list-style: none;
    font-size: 13.5px; color: var(--ink-body);
    line-height: 19.5px;
  }
  .contact-list li { display: flex; align-items: center; gap: 7px; }
  .contact-list svg { width: 11px; height: 11px; fill: #444; flex: none; }
  .brand-block {
    position: absolute; left: 338px; top: 88px;
  }
  .brand-name {
    display: flex; align-items: center; gap: 8px;
    font-weight: 700; font-size: 24px; letter-spacing: 0.5px;
    color: var(--ink-dark);
  }
  .brand-mark { width: 14px; height: 14px; background: var(--brand-red); flex: none; }
  .motto {
    margin-top: 46px;
    font-family: "Roboto Condensed", "Roboto", Arial, sans-serif;
    font-weight: 700; font-size: 15.5px; line-height: 18px;
    color: var(--ink-dark);
    display: inline-block;
    padding-bottom: 4px;
    border-bottom: 1px solid var(--rule-grey);
  }
  /* Back */
  .card--back {
    background: linear-gradient(180deg, var(--card-dark-top) 0%, var(--card-dark-top) 55%, var(--card-dark-bottom) 100%);
    display: flex; align-items: center; justify-content: center;
  }
  .brand-name--reverse {
    color: #ffffff; font-size: 30px;
    margin-top: -16px;
  }
  .brand-name--reverse .brand-mark { width: 18px; height: 18px; }
</style>
</head>
<body>
  <main class="sheet">
    <section class="card card--front" aria-label="Card front">
      <div class="accent-band"></div>
      <ul class="contact-list">
        <li>
          <svg viewBox="0 0 16 16" aria-hidden="true"><path d="M3.6 1.2 6 3.6c.4.4.4 1 0 1.4L4.8 6.2c.9 2 2.9 4 4.9 4.9L10.9 10c.4-.4 1-.4 1.4 0l2.4 2.4c.4.4.4 1 0 1.4l-1.3 1.3C11.6 16.9 0 5.4 2.2 1.3L3.6 1.2z"/></svg>
          (+61) 400512836
        </li>
        <li>
          <svg viewBox="0 0 16 16" aria-hidden="true"><path d="M1 3h14v10H1z M2.2 4.2 8 8.6l5.8-4.4z" fill-rule="evenodd"/></svg>
          info@Q7RServices.example
        </li>
        <li>
          <svg viewBox="0 0 16 16" aria-hidden="true"><path d="M8 1a7 7 0 1 0 0 14A7 7 0 0 0 8 1zm0 1.4c.8 0 1.7 1.7 2 4.1H6c.3-2.4 1.2-4.1 2-4.1zM2.5 7.3h2.6c0 .5 0 1 .1 1.4H2.5a5.6 5.6 0 0 1 0-1.4zm3.4 0h4.2a9 9 0 0 1 0 1.4H5.9a9 9 0 0 1 0-1.4zm5 0h2.6a5.6 5.6 0 0 1 0 1.4h-2.6c0-.4.1-.9 0-1.4zM6 9.5h4c-.3 2.4-1.2 4.1-2 4.1s-1.7-1.7-2-4.1z"/></svg>
          Q7RServices.example
        </li>
      </ul>
      <div class="brand-block">
        <div class="brand-name"><span class="brand-mark"></span>Q7R Services</div>
        <p class="motto">Sketch - Detail<br>Refine - Complete</p>
      </div>
    </section>

    <section class="card card--back" aria-label="Card back">
      <div class="brand-name brand-name--reverse"><span class="brand-mark"></span>Q7R Services</div>
    </section>
  </main>
</body>
</html>
```